Mobile Oil Change company needs a flyer to promote new business

We need a flyer to 1) print & handout and 2) email out to potential customers. We are a mobile oil change company that comes to our customer locations to perform the work instead of customers going to traditional oil change companies. We have a 21 point inspection with our oil change. (21 point inspection details will not be on the flyer). Would like to keep the flyer simple but creative. I'm attaching 1) the write-up we created, 2) our logo (logo color is dark teal on white but other combinations are included if you wanted to propose a different color combination), and 3) additional services we offer. Logo font is Alegreya Sans.
Would like the additional services listed with icons and brief descriptions (similar to attachment) without pricing. Company website for reference is www.brookmerelubeworks.com.

Target Market(s)

Companies with many service vehicles such as Oil & Gas service companies, heating and air conditioning companies, utility companies, police departments, etc. Companies that prioritize convenience and maintenance first.

Font styles to use
Sans Serif

Colors
00a990

Requirements
Must have
• Simple but creative design with our logo at top of the flyer. Additional Services (details in document supplied) can be smaller and less prominent than other "main" content listed in the CONTENT document supplied.
Should not have
• Do not use animated character graphics in the flyer and limit (1) stock photos to A small area in the flyer.

```html
<!DOCTYPE html>
<html lang="en">
<head>
<meta charset="utf-8">
<title>Brookmere Lube Works – Hassle Free Oil Changes</title>
<link rel="stylesheet" href="https://fonts.googleapis.com/css2?family=Montserrat:wght@500;600;700;800&display=swap">
<style>
  :root {
    --teal-deep: #164546;
    --teal-panel: #1b4e4d;
    --teal-brand: #00a990;
    --dot-teal: #2bb59b;
    --accent-yellow: #f4c430;
    --white: #ffffff;
    --photo-dark: #0d1a1c;
    --photo-mid: #2a3a3c;
  }
  * { margin: 0; padding: 0; box-sizing: border-box; }
  html, body { width: 927px; height: 1200px; overflow: hidden; background: var(--white); }
  body { font-family: "Montserrat", Arial, sans-serif; color: var(--white); }
  .flyer { position: relative; width: 927px; height: 1200px; overflow: hidden; background: var(--white); }
  .backdrop { position: absolute; inset: 0; }

  .brand {
    position: absolute; left: 650px; top: 52px; width: 250px;
    color: var(--teal-deep); font-weight: 800; font-size: 27px; line-height: 1.1;
    letter-spacing: 1px; display: flex; align-items: center; gap: 12px;
  }
  .brand-mark { width: 16px; height: 16px; background: var(--teal-deep); flex: none; }

  .process { position: absolute; left: 28px; top: 26px; width: 600px; }
  .process-title {
    font-weight: 700; font-size: 19px; line-height: 31px; font-variant: small-caps; letter-spacing: .3px;
  }
  .process-title .highlight { color: var(--accent-yellow); }
  .process-steps { list-style: none; margin-top: 22px; }
  .process-steps li {
    font-weight: 600; font-size: 14px; line-height: 22px; font-variant: small-caps; letter-spacing: .2px;
  }
  .process-steps li::before { content: "\2022"; margin-right: 6px; }

  .headline {
    position: absolute; left: 40px; top: 296px;
    font-weight: 700; font-size: 76px; line-height: 92px; letter-spacing: 2px; text-transform: uppercase;
  }

  .oil-claim {
    position: absolute; left: 15px; top: 584px;
    font-weight: 700; font-size: 27px; line-height: 44px; text-transform: uppercase;
  }
  .oil-claim .highlight, .inspection .highlight { color: var(--accent-yellow); }

  .dots { position: absolute; left: 273px; width: 427px; border-top: 4px dotted var(--dot-teal); }
  .dots.upper { top: 686px; }
  .dots.lower { top: 752px; }
  .inspection {
    position: absolute; left: 88px; top: 701px;
    font-weight: 700; font-size: 28px; text-transform: uppercase; white-space: nowrap;
  }

  .extras-title {
    position: absolute; left: 164px; top: 778px;
    color: var(--accent-yellow); font-weight: 700; font-size: 20px; text-transform: uppercase;
  }

  .service { position: absolute; display: flex; align-items: center; gap: 14px; }
  .service svg { width: 40px; height: 40px; flex: none; }
  .service p { font-weight: 700; font-size: 13px; line-height: 20px; }
</style>
</head>
<body>
<main class="flyer">
  <svg class="backdrop" width="927" height="1200" viewBox="0 0 927 1200" aria-hidden="true">
    <defs>
      <linearGradient id="engine-tone" x1="0" y1="0" x2="1" y2="1">
        <stop offset="0" stop-color="#2a3a3c"/>
        <stop offset=".5" stop-color="#0d1a1c"/>
        <stop offset="1" stop-color="#1e2c2e"/>
      </linearGradient>
    </defs>
    <polygon points="0,0 447,0 927,500 927,1200 500,1200 0,690" fill="#1b4e4d"/>
    <polygon points="0,0 447,0 719,283 0,283" fill="#164546"/>
  </svg>
  <svg class="backdrop" width="927" height="1200" viewBox="0 0 927 1200" role="img" aria-label="Dark photo of an engine bay behind the headline">
    <polygon points="0,283 719,283 927,500 927,573 0,573" fill="url(#engine-tone)"/>
  </svg>

  <div class="brand"><span class="brand-mark"></span><span>BROOKMERE LUBE WORKS</span></div>

  <section class="process">
    <h2 class="process-title">Our simple 5-step process<br>lets you schedule an appointment<br>and get service to <span class="highlight">save time and money</span>:</h2>
    <ul class="process-steps">
      <li>Call or email us to schedule service</li>
      <li>Our highly trained technicians come to you for service</li>
      <li>Service is performed quickly on your vehicle</li>
      <li>Pay agreed-upon pricing and receipt is emailed to you</li>
      <li>Services performed are tracked electronically and reminders created</li>
    </ul>
  </section>

  <h1 class="headline">Hassle Free<br>Oil Changes<br>On Your Terms</h1>

  <p class="oil-claim"><span class="highlight">High quality</span> synthetic oil used is best suited<br>for commercial vehicles</p>

  <div class="dots upper"></div>
  <p class="inspection">Service includes a <span class="highlight">21-point inspection</span></p>
  <div class="dots lower"></div>

  <h3 class="extras-title">Additional services are available</h3>

  <div class="service" style="left:222px; top:818px;">
    <svg viewBox="0 0 40 40" fill="none" stroke="#fff" stroke-width="2"><rect x="6" y="6" width="28" height="28"/><path d="M12 6v28M17 6v28M23 6v28M28 6v28"/></svg>
    <p>Maintain optimum engine performance.<br>Recommended every 15,000-30,000 miles.</p>
  </div>
  <div class="service" style="left:280px; top:884px;">
    <svg viewBox="0 0 40 40" fill="none" stroke="#fff" stroke-width="2"><rect x="6" y="6" width="28" height="28" rx="5"/><path d="M11 15c6-4 12 4 18 0M11 21c6-4 12 4 18 0M11 27c6-4 12 4 18 0"/></svg>
    <p>Maintain a clean A/C and fan system.<br>Recommended every 12 months or 15,000-25,000 miles.</p>
  </div>
  <div class="service" style="left:338px; top:950px;">
    <svg viewBox="0 0 40 40" fill="none" stroke="#fff" stroke-width="2"><path d="M5 28C8 14 32 14 35 28Z"/><path d="M20 28l-9-12"/><path d="M20 32v4"/></svg>
    <p>Maintain excellent visibility on the road.<br>Recommended every 6-12 months.</p>
  </div>
  <div class="service" style="left:405px; top:1010px;">
    <svg viewBox="0 0 40 40" fill="none" stroke="#fff" stroke-width="2"><circle cx="20" cy="20" r="15"/><circle cx="20" cy="20" r="5"/><path d="M5 18h10M25 18h10M20 25v10"/></svg>
    <p>Maintain proper power steering system health.<br>Recommended every 30,000-60,000 miles.</p>
  </div>
  <div class="service" style="left:474px; top:1078px;">
    <svg viewBox="0 0 40 40" fill="none" stroke="#fff" stroke-width="2"><rect x="9" y="6" width="15" height="28" rx="2"/><rect x="12" y="10" width="9" height="7"/><path d="M24 14l6 5v11a2 2 0 0 0 4 0V16l-4-5"/></svg>
    <p>Clean your fuel system and injectors to<br>improve fuel economy.</p>
  </div>
  <div class="service" style="left:538px; top:1140px;">
    <svg viewBox="0 0 40 40" fill="none" stroke="#fff" stroke-width="2"><circle cx="20" cy="20" r="14"/><circle cx="20" cy="20" r="5"/><path d="M20 9v2M20 29v2M9 20h2M29 20h2"/></svg>
    <p>Maintain an excellent functional brake system.<br>Recommended every 2 years or 20,000 miles</p>
  </div>
</main>
</body>
</html>
```